Real estate business card

I need a business card for my real estate company. I help clients buy and sell properties. I would like to keep the design very simple and professional. I would like the design to convey professionalism, safety and trust. I prefer no graphics but a simple logo design would be nice if that is part of what you do.
Updates

Please keep the designs simple. No high-rise buildings please. 

Reason: My design has not been finalized.

Target Market(s)

Age group 30-60 mostly affluent

Industry/Entity Type

Real Estate

Contact Information for Business Card

Velmont Realtors
Howard Prisk, Broker
4153 Marlow Ave. #226, La Crescenta, CA 91207

Requirements
Nice to have
• Logo can be combination of my initials HP or just Z or a simple geometric shape? Please see "Desig Ideas" attachment. No pics of houses or shaking hands, dollar bills, $, %, etc...
Please use fonts similar to Helvetica for a clean, modern look (think Northern European design, simple, clean yet bold)

Also use font colors such as blue, grey in different shades. Use pastel colors if better.

```html
<!DOCTYPE html>
<html lang="en">
<head>
<meta charset="utf-8">
<title>Velmont Realtors – Business Card</title>
<link rel="stylesheet" href="https://fonts.googleapis.com/css2?family=Cinzel:wght@400;600&family=Exo+2:wght@400;500&display=swap">
<style>
  :root {
    --backdrop: #e4e6e9;
    --card: #fbfbfb;
    --card-shade: #ececec;
    --panel: #323234;
    --accent-blue: #4d86bf;
    --ink: #2a2a2c;
    --ink-soft: #3a3a3d;
    --on-dark: #f2f2f2;
  }
  * { margin: 0; padding: 0; box-sizing: border-box; }
  html, body {
    width: 1200px; height: 899px; overflow: hidden;
    background: var(--backdrop);
  }
  .card {
    position: absolute; left: 100px; top: 164px;
    width: 1000px; height: 571px;
    background: radial-gradient(ellipse at 45% 40%, var(--card) 40%, var(--card-shade) 100%);
    box-shadow: 0 14px 40px rgba(0,0,0,0.18);
    overflow: hidden;
  }
  .panel { position: absolute; inset: 0; width: 1000px; height: 571px; }
  .brand {
    position: absolute; left: 80px; top: 150px;
    font-family: "Cinzel", "Times New Roman", serif;
    font-weight: 400; font-size: 44px; letter-spacing: 1px;
    color: var(--ink);
  }
  .address {
    position: absolute; left: 84px; top: 255px;
    font-family: "Exo 2", "Helvetica", sans-serif;
    font-size: 23px; line-height: 32px; letter-spacing: 1.5px;
    color: var(--ink);
  }
  .contacts {
    position: absolute; left: 84px; top: 345px;
    list-style: none;
    font-family: "Exo 2", "Helvetica", sans-serif;
    font-size: 22px; letter-spacing: 1.5px; color: var(--ink-soft);
  }
  .contacts li { display: flex; align-items: center; height: 35px; }
  .contacts svg { width: 22px; height: 22px; margin-right: 14px; fill: var(--ink-soft); }
  .person {
    position: absolute; right: 52px; top: 288px; text-align: right;
    font-family: "Exo 2", "Helvetica", sans-serif; color: var(--on-dark);
  }
  .person-name { font-size: 28px; font-weight: 500; letter-spacing: 2px; }
  .person-title { font-size: 17px; letter-spacing: 2.5px; margin-top: 4px; }
</style>
</head>
<body>
<div class="card">
  <svg class="panel" viewBox="0 0 1000 571" aria-hidden="true">
    <path d="M700 0 C 650 170, 665 410, 750 571 L 768 571 C 684 410, 668 170, 718 0 Z" fill="var(--accent-blue)"/>
    <path d="M718 0 C 668 170, 682 410, 766 571 L 1000 571 L 1000 0 Z" fill="var(--panel)"/>
  </svg>

  <h1 class="brand">Velmont Realtors</h1>

  <p class="address">4153 Marlow Ave. #226,<br>La Crescenta</p>

  <ul class="contacts">
    <li><svg viewBox="0 0 24 24"><path d="M6.6 10.8a15 15 0 0 0 6.6 6.6l2.2-2.2c.3-.3.7-.4 1-.2 1.1.4 2.3.6 3.6.6.6 0 1 .4 1 1V20c0 .6-.4 1-1 1A17 17 0 0 1 3 4c0-.6.4-1 1-1h3.5c.6 0 1 .4 1 1 0 1.3.2 2.5.6 3.6.1.3 0 .7-.2 1z"/></svg>818 402 7719</li>
    <li><svg viewBox="0 0 24 24"><path d="M7 1h10a2 2 0 0 1 2 2v18a2 2 0 0 1-2 2H7a2 2 0 0 1-2-2V3a2 2 0 0 1 2-2zm0 3v14h10V4zm5 15.5a1 1 0 1 0 0 2 1 1 0 0 0 0-2z"/></svg>818 402 7720</li>
    <li><svg viewBox="0 0 24 24"><path d="M7 2h8l3 3v5H7zM3 11h18v11H3zm3 3v2h3v-2zm5 0v2h3v-2zm5 0v2h2v-2zm-10 4v2h3v-2zm5 0v2h3v-2z"/></svg>818 402 7721</li>
    <li><svg viewBox="0 0 24 24"><path d="M2 5h20v14H2zm2 2v.5l8 5.5 8-5.5V7zm0 3v7h16v-7l-8 5.5z"/></svg>office@velmontmail.com</li>
    <li><svg viewBox="0 0 24 24"><path d="M12 2a10 10 0 1 0 0 20 10 10 0 0 0 0-20zm0 2c.9 0 2.2 1.9 2.8 5H9.2C9.8 5.9 11.1 4 12 4zM8.3 4.8A12 12 0 0 0 7.2 9H4.9a8 8 0 0 1 3.4-4.2zm7.4 0A8 8 0 0 1 19.1 9h-2.3a12 12 0 0 0-1.1-4.2zM4.3 11h2.7a18 18 0 0 0 0 2H4.3a8 8 0 0 1 0-2zm4.7 0h6a16 16 0 0 1 0 2H9a16 16 0 0 1 0-2zm8 0h2.7a8 8 0 0 1 0 2H17a18 18 0 0 0 0-2zM4.9 15h2.3c.2 1.6.6 3 1.1 4.2A8 8 0 0 1 4.9 15zm4.3 0h5.6c-.6 3.1-1.9 5-2.8 5s-2.2-1.9-2.8-5zm7.6 0h2.3a8 8 0 0 1-3.4 4.2c.5-1.2.9-2.6 1.1-4.2z"/></svg>www.velmontrealtors.com</li>
  </ul>

  <div class="person">
    <p class="person-name">GRANT ELLERY</p>
    <p class="person-title">FINANCIAL ADVISOR</p>
  </div>
</div>
</body>
</html>
```